Store Front Sign for Vape Store

Interested in getting a store front sign graphic done. Sign is for over the door (lighted sign). Dimensions of sign: 6 feet long x 2 feet high.
Sign is for a Vape Store. I have attached the logo to be used.
Looking for a modern and professional look
Phone numbers to be used.
Whatsapp# 364-9105
Contact #519-7036
Sign should have Instagram & Facebook logos and. handle @lagoonmistco

Industry/Entity Type

Vape | Electronic Cigarettes

Colors

Designer to choose colors to be used in the design.

Requirements
Must have
• Facebook and Instagram Logos. Contact Numbers.
Should not have
• Any Persons.

```html
<!DOCTYPE html>
<html lang="en">
<head>
<meta charset="utf-8">
<title>Lagoon Mist Co – Storefront Sign</title>
<link rel="stylesheet" href="https://fonts.googleapis.com/css2?family=Montserrat:wght@500;600&display=swap">
<style>
  :root {
    --page: #eef0f2;
    --panel-dark: #2f2d2e;
    --panel-mid: #3a3839;
    --corner-white: #f4f5f6;
    --corner-shade: #c9ccd0;
    --swoosh-cyan: #00c2ec;
    --swoosh-blue: #0a7fd6;
    --edge-black: #1b1a1b;
    --text-light: #f2f4f5;
    --name-silver: #dfe3e6;
    --icon-fill: #1aa8d8;
  }
  html, body {
    margin: 0;
    width: 1200px;
    height: 889px;
    overflow: hidden;
    background: var(--page);
  }
  .sign {
    position: absolute;
    left: 40px;
    top: 258px;
    width: 1120px;
    height: 373px;
    font-family: "Montserrat", sans-serif;
  }
  .sign-art {
    position: absolute;
    inset: 0;
    width: 1120px;
    height: 373px;
  }
  .brand-name {
    position: absolute;
    left: 0;
    right: 0;
    top: 128px;
    margin: 0;
    text-align: center;
    font-weight: 600;
    font-size: 54px;
    letter-spacing: 1px;
    color: var(--name-silver);
  }
  .contact-row {
    position: absolute;
    left: 262px;
    top: 310px;
    display: flex;
    align-items: center;
    gap: 34px;
    color: var(--text-light);
    font-weight: 500;
    font-size: 24px;
  }
  .contact-item {
    display: flex;
    align-items: center;
    gap: 12px;
  }
  .icon-dot {
    width: 30px;
    height: 30px;
    border-radius: 50%;
    background: var(--icon-fill);
    display: inline-flex;
    align-items: center;
    justify-content: center;
  }
  .social-dots {
    display: flex;
    gap: 8px;
  }
  .handle {
    font-size: 22px;
  }
</style>
</head>
<body>
  <section class="sign">
    <svg class="sign-art" viewBox="0 0 1120 373" xmlns="http://www.w3.org/2000/svg">
      <defs>
        <linearGradient id="corner-grad" x1="0" y1="0" x2="1" y2="1">
          <stop offset="0" stop-color="var(--corner-white)"/>
          <stop offset="1" stop-color="var(--corner-shade)"/>
        </linearGradient>
        <linearGradient id="panel-grad" x1="0" y1="0" x2="1" y2="0">
          <stop offset="0" stop-color="var(--panel-mid)"/>
          <stop offset="0.6" stop-color="var(--panel-dark)"/>
          <stop offset="1" stop-color="#1f1e1f"/>
        </linearGradient>
        <linearGradient id="swoosh-grad" x1="0" y1="1" x2="1" y2="0">
          <stop offset="0" stop-color="var(--swoosh-blue)"/>
          <stop offset="1" stop-color="var(--swoosh-cyan)"/>
        </linearGradient>
      </defs>
      <rect class="corner-base" width="1120" height="373" fill="url(#corner-grad)"/>
      <path class="swoosh-top" d="M0,120 C60,60 160,14 285,0 L320,0 C190,26 70,100 0,200 Z" fill="var(--swoosh-cyan)"/>
      <path class="edge-top" d="M0,118 C60,58 160,12 285,-2" fill="none" stroke="var(--edge-black)" stroke-width="4"/>
      <path class="panel-body" role="img" aria-label="Dark hexagonal honeycomb texture"
            d="M320,0 L1120,0 L1120,210 C1070,290 980,345 860,373 L0,373 L0,200 C70,100 190,26 320,0 Z"
            fill="url(#panel-grad)"/>
      <path class="swoosh-bottom" d="M1120,210 C1070,290 980,345 860,373 L930,373 C1030,345 1090,300 1120,262 Z" fill="url(#swoosh-grad)"/>
      <path class="edge-bottom" d="M1122,264 C1090,302 1030,347 930,375" fill="none" stroke="var(--edge-black)" stroke-width="4"/>
    </svg>

    <h1 class="brand-name">Lagoon Mist Co</h1>

    <div class="contact-row">
      <div class="contact-item">
        <span class="icon-dot">
          <svg width="16" height="16" viewBox="0 0 24 24" aria-hidden="true">
            <path d="M6.6 10.8a15.1 15.1 0 0 0 6.6 6.6l2.2-2.2a1 1 0 0 1 1-.25 11.4 11.4 0 0 0 3.6.57 1 1 0 0 1 1 1V20a1 1 0 0 1-1 1A17 17 0 0 1 3 4a1 1 0 0 1 1-1h3.5a1 1 0 0 1 1 1c0 1.25.2 2.45.57 3.57a1 1 0 0 1-.25 1z" fill="#ffffff"/>
          </svg>
        </span>
        <span class="phone">519-7036</span>
      </div>
      <div class="contact-item">
        <span class="icon-dot"></span>
        <span class="phone">364-9105</span>
      </div>
      <div class="contact-item">
        <span class="social-dots">
          <span class="icon-dot"></span>
          <span class="icon-dot"></span>
        </span>
        <span class="handle">@lagoonmistco</span>
      </div>
    </div>
  </section>
</body>
</html>
```